Wordpress Template Design using existing Logo and Colors

We are wanting a wordpress theme designing for our b2b marketing consultancy business. A comprehesive and elagant design to our current site www.pelvarogroup.com would be good.

Industry/Entity Type

Marketing

Font styles to use
Sans Serif

```html
<!DOCTYPE html>
<html lang="en">
<head>
<meta charset="utf-8">
<title>Pelvaro — B2B Data, Analytics and Marketing</title>
<link rel="stylesheet" href="https://fonts.googleapis.com/css2?family=Open+Sans:wght@400;600;700;800&display=swap">
<style>
:root{
  --red:#e3131b;
  --red-dark:#c10d14;
  --ink:#1f1f1f;
  --text:#444;
  --muted:#8a8a8a;
  --slate:#535f78;
  --dark:#222;
  --light:#f4f4f4;
  --white:#fff;
}
*{box-sizing:border-box;margin:0;padding:0}
html,body{width:1200px;height:4215px;overflow:hidden}
body{font-family:"Open Sans",Arial,sans-serif;color:var(--text);background:var(--white);position:relative}
.abs{position:absolute}
.btn{position:absolute;display:inline-block;background:var(--red);color:var(--white);font-weight:700;font-size:15px;letter-spacing:.5px;padding:0 26px;height:32px;line-height:32px;border-radius:6px;text-transform:uppercase}
.section-title{font-size:27px;font-weight:800;color:var(--ink);letter-spacing:.5px;text-transform:uppercase}

/* header */
.site-header{position:absolute;top:0;left:0;width:1200px;height:121px;background:var(--white)}
.brand{position:absolute;left:0;width:1200px;top:38px;text-align:center;font-size:34px;font-weight:800;color:var(--red);letter-spacing:2px}
.brand span.dot{display:inline-block;width:12px;height:12px;background:var(--ink);margin-left:6px;vertical-align:8px}
.menu-toggle{position:absolute;right:42px;top:50px;width:18px}
.menu-toggle i{display:block;height:3px;background:var(--red);margin-bottom:4px}

/* hero */
.hero{position:absolute;top:121px;left:0;width:1200px;height:582px;background:linear-gradient(180deg,#8a7a68 0%,#5a5048 40%,#2e2b2a 100%)}
.hero-title{position:absolute;top:306px;left:0;width:1200px;text-align:center;color:var(--white);font-size:21px;font-weight:800;letter-spacing:.5px}
.hero-sub{position:absolute;top:340px;left:420px;width:360px;text-align:center;color:var(--white);font-size:15px;line-height:20px}
.hero .btn{top:393px;left:532px;height:32px;font-size:13px;padding:0 28px}
.hero-arrow{position:absolute;top:312px;width:24px;height:24px;border:2px solid var(--white);border-radius:50%}
.hero-arrow svg{display:block;margin:5px}
.hero-dots{position:absolute;top:564px;left:574px}
.hero-dots i{display:inline-block;width:10px;height:10px;margin-right:6px;background:#bbb}
.hero-dots i.on{background:var(--red)}

/* services */
.service{position:absolute;top:711px;width:216px;height:216px;background:var(--light);border-radius:8px;text-align:center;box-shadow:0 2px 6px rgba(0,0,0,.12)}
.service svg{margin-top:28px}
.service h3{font-size:16px;font-weight:700;color:var(--ink);margin-top:10px;text-transform:uppercase}
.service p{font-size:14px;line-height:17px;margin:6px 22px 0;color:var(--ink)}
.service .more{font-size:12px;color:var(--ink);margin-top:6px}
.service .more b{display:inline-block;width:12px;height:12px;border-radius:50%;background:var(--red);vertical-align:-2px;margin-left:3px}
.service.active{background:var(--red);top:711px}
.service.active h3,.service.active p,.service.active .more{color:var(--white)}
.service.active .more b{background:var(--white)}

.intro{position:absolute;top:990px;left:270px;width:660px;text-align:center;font-size:14px;line-height:19px;color:var(--text)}

/* target marketing */
.feature-text{position:absolute;font-size:14.5px;line-height:19px;color:var(--ink)}
.checklist{position:absolute;display:grid;grid-template-columns:230px 230px;row-gap:11px;font-size:14px;font-weight:700;color:var(--ink);text-transform:uppercase}
.checklist li{list-style:none}
.checklist li:before{content:"\25B8";margin-right:8px}
.checklist li.hot{color:var(--red)}
.photo{position:absolute}

/* data band */
.data-band{position:absolute;top:1582px;left:0;width:1200px;height:528px;background:var(--slate)}
.data-band .section-title{color:var(--white);font-size:24px}
.data-band .feature-text,.data-band .checklist{color:var(--white)}

/* blog */
.blog-title{position:absolute;top:2189px;left:0;width:1200px;text-align:center}
.blog-sub{position:absolute;top:2224px;left:0;width:1200px;text-align:center;font-size:13px;color:var(--muted)}
.post{position:absolute;width:470px;height:140px}
.post .thumb{position:absolute;left:0;top:0;width:160px;height:140px}
.post h4{position:absolute;left:184px;top:0;font-size:17px;font-weight:700;color:var(--ink)}
.post .meta{position:absolute;left:184px;top:26px;width:270px;font-size:12px;color:var(--ink)}
.post .meta span{float:right}
.post p{position:absolute;left:184px;top:45px;width:270px;font-size:13px;line-height:17px;color:var(--ink)}

/* brochure */
.brochure{position:absolute;top:2745px;left:0;width:1200px;height:310px;background:linear-gradient(90deg,var(--red) 0%,#ee2a2f 100%)}
.pdf-badge{position:absolute;left:167px;top:71px;width:184px;height:184px;border-radius:50%;background:#f4f4f4}
.pdf-badge .pdf{position:absolute;left:42px;top:110px;width:100px;height:44px;background:var(--red);color:var(--white);font-weight:800;font-size:24px;text-align:center;line-height:44px}
.pdf-badge .sheet{position:absolute;left:50px;top:32px;width:84px;height:84px;background:linear-gradient(135deg,#9aa0a8,#5d646d)}
.brochure h2{position:absolute;left:382px;top:108px;color:var(--white);font-size:23px;font-weight:800;text-transform:uppercase}
.brochure p{position:absolute;left:382px;top:144px;width:520px;color:var(--white);font-size:14px;line-height:18px;font-weight:600}
.download{position:absolute;left:386px;top:205px;height:32px;width:160px;background:#666;border-radius:4px;color:var(--white);font-size:13px;line-height:32px;padding-left:22px}
.download i{position:absolute;right:0;top:0;width:38px;height:32px;background:#555;border-radius:0 4px 4px 0}

/* case studies */
.cases{position:absolute;left:121px;top:3302px}
.cases li{list-style:none;height:45px;font-size:15px;font-weight:700;color:var(--ink)}
.cases li b{display:inline-block;width:28px;height:28px;border-radius:50%;background:var(--red);color:var(--white);text-align:center;line-height:28px;margin-right:10px;font-size:14px}

/* newsletter */
.newsletter h2{position:absolute;top:3640px;left:0;width:1200px;text-align:center;font-size:28px;font-weight:800;color:var(--ink);letter-spacing:.5px}
.newsletter p{position:absolute;top:3679px;left:0;width:1200px;text-align:center;font-size:14px;font-weight:600;color:var(--ink)}
.news-input{position:absolute;top:3718px;left:303px;width:454px;height:38px;border:1px solid #ccc;border-radius:6px 0 0 6px;font-size:14px;color:#999;line-height:36px;padding-left:16px}
.news-btn{position:absolute;top:3718px;left:757px;width:128px;height:38px;background:var(--red);color:var(--white);font-weight:700;font-size:15px;line-height:38px;text-align:center;border-radius:0 6px 6px 0}

/* footer */
.site-footer{position:absolute;top:3827px;left:0;width:1200px;height:332px;background:var(--dark);color:var(--white)}
.foot-brand{position:absolute;left:118px;top:48px;font-size:30px;font-weight:800;color:var(--red);letter-spacing:2px}
.foot-about{position:absolute;left:118px;top:110px;width:250px;font-size:12.5px;line-height:18px}
.foot-col h5{position:absolute;top:38px;font-size:15px;font-weight:700;text-transform:uppercase}
.foot-links{position:absolute;left:416px;top:80px;font-size:13px;line-height:21px}
.foot-links li{list-style:none}
.foot-links li:before{content:"\25B8";margin-right:12px}
.contact{position:absolute;font-size:12.5px;line-height:19px}
.contact div{position:relative;padding-left:28px;margin-bottom:8px}
.contact div i{position:absolute;left:2px;top:4px;width:10px;height:10px;border-radius:50%;background:var(--white)}
.legal{position:absolute;top:4159px;left:0;width:1200px;height:56px;background:var(--red);color:var(--white)}
.legal p{position:absolute;left:118px;top:19px;font-size:13px;font-weight:700}
.social{position:absolute;right:120px;top:14px}
.social i{display:inline-block;width:28px;height:28px;border-radius:50%;background:var(--white);margin-left:12px}
</style>
</head>
<body>

<header class="site-header">
  <div class="brand">PELVARO<span class="dot"></span></div>
  <div class="menu-toggle"><i></i><i></i><i></i></div>
</header>

<section class="hero">
  <div class="abs" role="img" aria-label="City skyline with skyscrapers at dusk" style="inset:0"></div>
  <div class="hero-arrow" style="left:48px"><svg width="10" height="10" viewBox="0 0 10 10"><path d="M7 1 3 5l4 4" stroke="#fff" stroke-width="2" fill="none"/></svg></div>
  <div class="hero-arrow" style="right:48px"><svg width="10" height="10" viewBox="0 0 10 10"><path d="M3 1l4 4-4 4" stroke="#fff" stroke-width="2" fill="none"/></svg></div>
  <h1 class="hero-title">INBOUND &amp; OUTBOUND CALL CENTERS</h1>
  <p class="hero-sub">Attract new leads, increase sales &amp; inspire customers through our in-country call centers network</p>
  <span class="btn">Learn More</span>
  <div class="hero-dots"><i class="on"></i><i></i><i></i></div>
</section>

<div class="service" style="left:124px">
  <svg width="50" height="46" viewBox="0 0 50 46" fill="none" stroke="#222" stroke-width="2"><ellipse cx="25" cy="8" rx="14" ry="5"/><path d="M11 8v24c0 3 6 5 14 5s14-2 14-5V8M11 20c0 3 6 5 14 5s14-2 14-5"/></svg>
  <h3>B2B Database</h3>
  <p>Get access to Asia's leading market &amp; bus...</p>
  <div class="more">Read More <b></b></div>
</div>
<div class="service active" style="left:374px">
  <svg width="50" height="46" viewBox="0 0 50 46" fill="none" stroke="#fff" stroke-width="2"><circle cx="25" cy="23" r="17"/><circle cx="25" cy="23" r="10"/><circle cx="25" cy="23" r="3"/><path d="M25 2v8M25 36v8M4 23h8M38 23h8"/></svg>
  <h3>Target Marketing</h3>
  <p>We develop tailored marketing solutio...</p>
  <div class="more">Read More <b></b></div>
</div>
<div class="service" style="left:621px">
  <svg width="50" height="46" viewBox="0 0 50 46" fill="none" stroke="#222" stroke-width="2"><path d="M10 28v-6a15 15 0 0 1 30 0v6"/><rect x="7" y="26" width="7" height="12" rx="2"/><rect x="36" y="26" width="7" height="12" rx="2"/><path d="M40 38c0 4-6 5-12 5"/></svg>
  <h3>Call Centre</h3>
  <p>When your business requires instantan...</p>
  <div class="more">Read More <b></b></div>
</div>
<div class="service" style="left:865px">
  <svg width="50" height="46" viewBox="0 0 50 46" fill="none" stroke="#222" stroke-width="2"><rect x="10" y="4" width="26" height="34" rx="2"/><circle cx="23" cy="17" r="5"/><path d="M15 32c1-5 4-8 8-8s7 3 8 8"/><circle cx="36" cy="36" r="6"/></svg>
  <h3>Data Management</h3>
  <p>We analyze your data and report on effec...</p>
  <div class="more">Read More <b></b></div>
</div>

<p class="intro">We are a B2B Data, Analytics and Marketing Consulting Company specialized in harnessing the power of potential data to strengthen connections between decision makers, companies and products. We focus on solutions engineered to solve distinct challenges in the data, direct marketing, and analytics space.</p>

<section>
  <h2 class="section-title abs" style="left:121px;top:1144px">Target Marketing</h2>
  <p class="feature-text" style="left:121px;top:1212px;width:470px">The old days of mass marketing doesn't work in a world where buyers are bombarded by hundreds of advertisements every day. Smart businesses are using targeted sales and marketing data to reach customers who are most likely to buy their products or services...</p>
  <ul class="checklist" style="left:121px;top:1318px">
    <li class="hot">Target Marketing</li><li>B2B Database</li>
    <li>Call Centre</li><li>Event Management</li>
    <li>Demand Generation</li><li>Lead Generation</li>
    <li>Marketing Automation</li><li>Market Research</li>
  </ul>
  <span class="btn" style="left:121px;top:1454px">Read More</span>
  <div class="photo" role="img" aria-label="Hand holding a magnifying glass over a network of people icons" style="left:627px;top:1150px;width:455px;height:353px;background:linear-gradient(135deg,#3f6f98 0%,#1c3550 60%,#0f1f30 100%)"></div>
</section>

<section class="data-band">
  <div class="photo" role="img" aria-label="Hands using a tablet showing charts over printed reports" style="left:121px;top:68px;width:455px;height:373px;background:linear-gradient(135deg,#dfe6ee 0%,#a9b8c8 55%,#6d7f94 100%)"></div>
  <h2 class="section-title abs" style="left:624px;top:78px">Data Management</h2>
  <p class="feature-text" style="left:624px;top:122px;width:470px;font-weight:700;font-size:13.5px;line-height:17px">We analyze your data and report on effective strategies for turning the data into a profitable resource....</p>
  <p class="feature-text" style="left:624px;top:166px;width:470px;font-size:13.5px;line-height:17px">Many organisations hold valuable customer data but they cannot put it to effective and profitable use due to inefficient processes and invalid data. In a good database, data is accurate,...</p>
  <ul class="checklist" style="left:624px;top:238px;grid-template-columns:248px 220px;row-gap:10px;font-size:13.5px">
    <li>Data Management</li><li>Data Quality Audit</li>
    <li>Data Cleansing</li><li>Data Processing</li>
    <li>Data Maintenance</li><li>Data Profiling</li>
    <li>Data Append</li><li>Data Localisation</li>
  </ul>
  <span class="btn" style="left:624px;top:389px">Read More</span>
</section>

<section>
  <h2 class="section-title blog-title">Blog</h2>
  <p class="blog-sub">Lorem Ipsum is simply dummy text of the printing</p>

  <article class="post" style="left:135px;top:2282px">
    <div class="thumb" role="img" aria-label="Hand touching a glowing digital screen" style="background:linear-gradient(135deg,#c7d3df,#6f8296)"></div>
    <h4>LOREM IPSUM</h4>
    <div class="meta">By <b>Daniel Okafor</b><span>Feb 9th, 2018</span></div>
    <p>Lorem Ipsum is simply dummy text of the printing and typesetting industry. Lorem Ipsum has been the industry's standard dummy text.<br>Read More... <b style="color:var(--red)">&#9679;</b></p>
  </article>
  <article class="post" style="left:627px;top:2282px">
    <div class="thumb" role="img" aria-label="Data analysis graphics on a blue screen" style="background:linear-gradient(135deg,#e5ecf3,#5b7ea3)"></div>
    <h4>LOREM IPSUM</h4>
    <div class="meta">By <b>Daniel Okafor</b><span>Feb 9th, 2018</span></div>
    <p>Lorem Ipsum is simply dummy text of the printing and typesetting industry. Lorem Ipsum has been the industry's standard dummy text.<br>Read More... <b style="color:var(--red)">&#9679;</b></p>
  </article>
  <article class="post" style="left:135px;top:2459px">
    <div class="thumb" role="img" aria-label="Glowing blue technology network" style="background:linear-gradient(135deg,#1c4fa3,#061a44)"></div>
    <h4>LOREM IPSUM</h4>
    <div class="meta">By <b>Daniel Okafor</b><span>Feb 9th, 2018</span></div>
    <p>Lorem Ipsum is simply dummy text of the printing and typesetting industry. Lorem Ipsum has been the industry's standard dummy text.<br>Read More... <b style="color:var(--red)">&#9679;</b></p>
  </article>
  <article class="post" style="left:627px;top:2459px">
    <div class="thumb" role="img" aria-label="Business network of connected people icons" style="background:linear-gradient(135deg,#dbe4ee,#4a6a90)"></div>
    <h4>LOREM IPSUM</h4>
    <div class="meta">By <b>Daniel Okafor</b><span>Feb 9th, 2018</span></div>
    <p>Lorem Ipsum is simply dummy text of the printing and typesetting industry. Lorem Ipsum has been the industry's standard dummy text.<br>Read More... <b style="color:var(--red)">&#9679;</b></p>
  </article>

  <span class="btn" style="left:534px;top:2646px">View More</span>
</section>

<section class="brochure">
  <div class="pdf-badge">
    <div class="sheet" role="img" aria-label="Brochure cover preview"></div>
    <div class="pdf">PDF</div>
  </div>
  <h2>Corporate Brochure</h2>
  <p>Learn our leading target marketing and intelligent data management solutions to attain new customers for your niche products and services.</p>
  <div class="download">DOWNLOAD <i><svg width="38" height="32" viewBox="0 0 38 32"><path d="M19 9v10M14 15l5 5 5-5M12 23h14" stroke="#fff" stroke-width="2" fill="none"/></svg></i></div>
</section>

<section>
  <h2 class="section-title abs" style="left:121px;top:3168px;font-size:25px">Case Studies</h2>
  <p class="feature-text" style="left:121px;top:3233px;width:470px;font-size:14px">Read our case studies to find out what we have done for our clients</p>
  <ul class="cases">
    <li><b>1</b>Telecommunication Company</li>
    <li><b>2</b>Global Distribution Company</li>
    <li><b>3</b>Software Manufacturing Company</li>
    <li><b>4</b>Logistic Company</li>
  </ul>
  <span class="btn" style="left:121px;top:3486px">Read More</span>
  <svg class="abs" style="left:691px;top:3175px" width="391" height="340" viewBox="0 0 391 340">
    <g stroke="#ddd" stroke-width="1">
      <path d="M12 20H391M12 60H391M12 100H391M12 140H391M12 180H391M12 220H391M12 260H391M12 300H391"/>
      <path d="M52 0V332M92 0V332M132 0V332M172 0V332M212 0V332M252 0V332M292 0V332M332 0V332M372 0V332"/>
    </g>
    <path d="M12 0V332H391" stroke="#222" stroke-width="3" fill="none"/>
    <g stroke="#222" stroke-width="2"><path d="M32 326v12M52 326v12M72 326v12M92 326v12M112 326v12M132 326v12M152 326v12M172 326v12M192 326v12M212 326v12M232 326v12M252 326v12M272 326v12M292 326v12M312 326v12M332 326v12M352 326v12"/></g>
    <polyline points="68,267 144,239 200,183 256,132 298,79" fill="none" stroke="#222" stroke-width="3"/>
    <g fill="#e3131b" stroke="#222" stroke-width="2">
      <circle cx="68" cy="267" r="10"/><circle cx="144" cy="239" r="10"/><circle cx="200" cy="183" r="10"/><circle cx="256" cy="132" r="10"/><circle cx="298" cy="79" r="10"/>
    </g>
  </svg>
</section>

<section class="newsletter">
  <h2>SUBSCRIBE TO OUR NEWSLETTER</h2>
  <p>To Receive The latest News And Update</p>
  <div class="news-input">Your E-Mail</div>
  <div class="news-btn">SUBMIT</div>
</section>

<footer class="site-footer">
  <div class="foot-brand">PELVARO</div>
  <p class="foot-about">Pelvaro is the primary source of market intelligence focused on identifying business opportunities and key decision makers throughout Asia Pacific Region. We provide access to over 3.5 million profiled organizations...</p>

  <div class="foot-col"><h5 style="left:416px">Quick Link</h5></div>
  <ul class="foot-links">
    <li>Home</li><li>About us</li><li>Target Market</li><li>Data Management</li><li>Blog</li><li>Contact us</li>
  </ul>

  <div class="foot-col"><h5 style="left:582px">Global HQ</h5></div>
  <div class="contact" style="left:582px;top:80px;width:240px">
    <div><i></i>: 4410 Harbor View Lane, Suite 210, Westport, CA 90210-4400, USA</div>
    <div><i></i>: +1 (555) 014-2288</div>
    <div><i></i>: contact@pelvarogroup.com</div>
    <div><i></i>: Monday - Friday : 9AM - 6PM</div>
  </div>

  <div class="foot-col"><h5 style="left:857px">Regional HQ</h5></div>
  <div class="contact" style="left:857px;top:80px;width:240px">
    <div><i></i>: 18 Kallang Way, #07-04 Meridian Hub, Singapore 349201</div>
    <div><i></i>: +1 (555) 014-2288</div>
    <div><i></i>: contact.sg@pelvarogroup.com</div>
    <div><i></i>: Monday - Friday : 9AM - 6PM</div>
  </div>
</footer>

<div class="legal">
  <p>Copyright © PELVARO 2018. All Right Reserved.</p>
  <div class="social"><i></i><i></i><i></i><i></i><i></i></div>
</div>

</body>
</html>
```